Law Firm Website

I currently have a temporary site that I created myself at www.kbrandellegal.net (hosted by hostpivot). I am generally happy with the content.

My permanent website just has basic information right now: www.kbrandellegal.com (hosted by cloudperch). I want to take the general content from the temporary website and have a more professional looking website on the permanent website. I want it in Wordpress format. I want a link to my blog: www.rivetsand.com. I want it to work on pads and smart phones. My number and e-mail address should be available on every page. The idea is to feature the potential client more than the lawyer.
Updates

Several of the designs are good. I would like the front page to have my number and address at the top (and at the top of every page) and to identify my law firm as "Law Office of Karen J. Brandell". No need to include "kbrandellegal" as that is just the web address. I like showing the most recent blog posts on the front page. I don't need video. No need to emphasize office hours or map location on the front page (that could be under a contact button). My picture should be somewhere. I would like an image from Boston on the front page if we can find one that is not copyright protected. No images of gavels or scales of justice. See some of the sample websites I listed in previous messages. Thanks!

Reason: I need more time to evaluate designs.

Reason: Designers apparently misunderstood and provided design that was not wordpress.

Industry/Entity Type

Law Firm

```html
<!DOCTYPE html>
<html lang="en">
<head>
<meta charset="utf-8">
<title>Karen J. Brandell Law Office</title>
<link href="https://fonts.googleapis.com/css2?family=Quando&family=Quattrocento:wght@400;700&display=swap" rel="stylesheet">
<style>
:root{
  --red:#9e0b0f;
  --red-bright:#c00000;
  --ink:#555049;
  --ink-soft:#6b675f;
  --nav:#6f6a60;
  --rule:#7a766c;
  --beige:#e7e3d6;
  --beige-dark:#b8b09a;
  --paper:#fbfaf7;
  --white:#ffffff;
}
*{margin:0;padding:0;box-sizing:border-box}
html,body{width:922px;height:1200px;overflow:hidden;background:var(--white)}
.page{position:relative;width:900px;height:1172px;transform:scale(1.02444);transform-origin:0 0;font-family:"Quando",serif;color:var(--ink);background:linear-gradient(#fff 0,#f3f2ef 330px,#fff 360px)}
.abs{position:absolute}

/* header */
.brand{left:126px;top:16px;width:210px;text-align:center}
.brand-name{font-family:"Quattrocento",serif;font-size:25px;color:#6e6a62;letter-spacing:.5px;line-height:30px}
.brand-sub{font-family:"Quattrocento",serif;font-size:18px;color:#6e6a62;line-height:18px;margin-left:40px}
.header-rule{left:0;top:52px;height:3px;background:var(--rule)}
.contact{left:600px;top:9px;font-family:"Quattrocento",serif;font-size:11px;color:#6e6a62;line-height:14px}
.contact strong{font-size:16px;font-weight:400;letter-spacing:.5px}
.social{left:706px;top:44px;display:flex;gap:4px}
.social span{width:13px;height:13px;border-radius:2px}

/* nav */
.nav{left:124px;top:72px;width:655px;height:27px;display:flex;background:var(--nav)}
.nav a{font-size:9px;color:#fff;text-decoration:none;display:flex;align-items:center;justify-content:center;border-right:1px solid #8b867b;padding:0 9px;white-space:nowrap}
.nav a.home{width:40px}
.nav a.alt{background:var(--red)}

/* hero */
.hero{left:124px;top:110px;width:656px;height:232px;background:linear-gradient(90deg,#e9e2cc 0,#f2eedf 26%,#c9cfd2 45%,#8c97a0 70%,#b9c4c9 100%);box-shadow:0 12px 20px rgba(0,0,0,.08)}
.hero-portrait{left:0;top:0;width:170px;height:232px;background:radial-gradient(ellipse at 55% 45%,#8d8f98 0,#b9b4a6 55%,#ede6d0 80%)}
.hero-copy{left:301px;top:138px;font-size:11.5px;line-height:16.7px;color:var(--red);width:230px}
.hero-btn{left:302px;top:285px;width:144px;height:29px;border:1px solid #d8d2bf;background:#f9f7ef;border-radius:3px;font-family:"Quattrocento",serif;font-size:13px;color:#6e6a62;letter-spacing:1px;padding:7px 0 0 12px}
.hero-btn i{position:absolute;right:8px;top:6px;width:16px;height:16px;background:#a9a393;border-radius:2px}

/* services */
.service{top:345px;height:166px;padding:30px 0 0 0}
.service h2{font-size:15px;font-weight:400;color:var(--red);line-height:16px}
.service p{font-size:8.5px;color:var(--ink-soft);margin-top:12px;line-height:12px}
.divider{top:345px;width:1px;height:166px;background:#e4e1d8}
.btn-red{width:107px;height:23px;background:var(--red-bright);color:#fff;font-family:Arial,sans-serif;font-size:8px;font-weight:700;display:flex;align-items:center;justify-content:center;border-radius:2px}

/* band */
.band{left:0;top:512px;width:900px;height:176px;background:linear-gradient(90deg,var(--beige-dark) 0,#d7d0bd 10%,var(--paper) 12%,var(--paper) 87%,#d7d0bd 89%,var(--beige-dark) 100%)}
.band-copy{left:131px;top:556px;width:420px;font-size:11px;line-height:14.5px;color:#7a766c}
.band-quote{left:580px;top:550px;width:200px;font-size:14.5px;line-height:16px;color:var(--red)}

/* posts */
.date{width:38px;height:38px;background:var(--red);border-radius:6px;color:#fff;text-align:center;font-family:Arial,sans-serif;font-weight:700;padding-top:7px}
.date small{display:block;font-size:6.5px;line-height:8px}
.date span{display:block;font-size:11px;line-height:12px}
.post-title{font-size:15px;color:var(--red)}
.post-body{width:440px;font-family:"Quattrocento",serif;font-weight:700;font-size:8.5px;line-height:10.3px;color:#5e5a52}
.post-rule{height:2px;background:#a7a08c}
.view-all{font-family:Arial,sans-serif;font-size:8px;color:var(--red);background:#fff;padding:0 8px}

/* blog box */
.blog{left:574px;top:719px;width:206px;height:305px;border:1px solid #ddd;background:#fff}
.blog-art{left:0;top:0;width:204px;height:50px;background:linear-gradient(#e3e3e1,#c9c9c6)}
.blog-name{left:20px;top:8px;font-family:"Quando",serif;font-size:28px;color:#111;letter-spacing:1px}
.blog-bar{left:0;top:50px;width:204px;height:20px;background:var(--red);color:#fff;font-family:Arial,sans-serif;font-weight:700;font-size:9px;display:flex;align-items:center;justify-content:center}
.blog-inner{left:0;top:70px;width:204px;height:220px;background:repeating-linear-gradient(#fff 0,#fff 9px,#f1f1f1 10px)}
.blog-head{left:34px;top:106px;width:164px;font-family:Arial,sans-serif;font-weight:700;font-size:8.5px;line-height:11px;color:var(--red)}
.blog-meta{left:36px;top:147px;font-family:Arial,sans-serif;font-size:7.5px;line-height:9px;color:#222}
.blog-text{left:12px;top:170px;width:186px;font-family:Arial,sans-serif;font-size:7.3px;line-height:9.3px;color:#111}
.blog-foot{left:4px;top:293px;width:200px;font-family:Arial,sans-serif;font-size:8px;color:#222;display:flex;justify-content:space-between}
.blog-foot a{color:#2a4a8a;font-size:7px}

/* footer */
.foot-nav{left:0;top:1030px;width:900px;height:46px;border-top:1px solid #e5e3de;border-bottom:2px solid #dcd9d2;display:flex;justify-content:center;align-items:center;font-family:"Quattrocento",serif;font-size:10px;color:#6b675f;gap:10px}
.foot-contact{left:116px;top:1095px;font-family:"Quattrocento",serif;font-size:12px;color:#6b675f}
.foot-contact b{color:var(--red);font-size:13px;margin:0 8px 0 8px}
.foot-contact u{margin-left:12px}
.foot-brand{left:610px;top:1085px;width:170px;text-align:right;font-family:"Quattrocento",serif;color:var(--red);font-size:18px;line-height:18px}
.foot-brand small{display:block;font-size:12.5px;color:#6e6a62;line-height:16px}
.legal{left:0;top:1124px;width:900px;height:48px;background:var(--beige);font-family:"Quattrocento",serif;font-size:8px;color:#444;padding:17px 0 0 115px}
.legal u{color:#2a4a8a}
</style>
</head>
<body>
<div class="page">

  <header>
    <div class="abs header-rule" style="left:0;width:176px"></div>
    <div class="abs header-rule" style="left:283px;width:617px"></div>
    <div class="abs brand">
      <div class="brand-name">Karen J. Brandell</div>
      <div class="brand-sub">Law Office</div>
    </div>
    <svg class="abs" style="left:562px;top:9px" width="36" height="28" viewBox="0 0 36 28" aria-hidden="true">
      <rect x="4" y="14" width="26" height="12" rx="2" fill="#5a564f"/>
      <path d="M2 10 Q17 -2 32 10 L28 14 L22 11 L12 11 L6 14 Z" fill="#3d3a35"/>
      <circle cx="17" cy="20" r="3.5" fill="#d9d5cb"/>
    </svg>
    <div class="abs contact">Phone: <strong>617 555-0142</strong><br>Email: kbrandell@kbrandellegal.com</div>
    <div class="abs social">
      <span style="background:#3b5b98"></span><span style="background:#3aa1d8"></span><span style="background:#2b7bb9"></span><span style="background:#e8912c"></span>
    </div>
  </header>

  <nav class="abs nav">
    <a class="home" href="#"><svg width="10" height="9" viewBox="0 0 10 9"><path d="M5 0 L10 4.5 H8.5 V9 H1.5 V4.5 H0 Z" fill="#fff"/></svg></a>
    <a href="#">Why Hire Me?</a>
    <a href="#">Success Stories</a>
    <a href="#">Practice Areas</a>
    <a href="#">Representative Clients</a>
    <a href="#">Services Provided</a>
    <a class="alt" href="#">Contact Us</a>
    <a class="alt" href="#" style="flex:1;border:none">How To Find Us</a>
  </nav>

  <section class="abs hero" role="img" aria-label="Aerial view of the Boston city skyline">
    <div class="abs hero-portrait" role="img" aria-label="Portrait of the attorney"></div>
  </section>
  <p class="abs hero-copy">Your business is under constant attack. With more success, you become more of a target. Whether it's keeping you out of a lawsuit or defending one that you are already in (or prosecuting one when necessary), I'm here to help.</p>
  <div class="abs hero-btn">LEARN MORE<i></i></div>

  <section>
    <div class="abs service" style="left:131px;width:205px">
      <h2>Employment Counseling and Litigation</h2>
      <p>Employment Counseling<br>and Litigation</p>
    </div>
    <div class="abs divider" style="left:343px"></div>
    <div class="abs service" style="left:357px;width:200px">
      <h2>Business Litigation, Contracts, Counseling</h2>
      <p>Business Litigation, Contracts<br>Counseling</p>
    </div>
    <div class="abs divider" style="left:561px"></div>
    <div class="abs service" style="left:587px;width:190px">
      <h2>Have questions or would like to make an appointment?</h2>
    </div>
    <div class="abs btn-red" style="left:179px;top:464px">Learn More »</div>
    <div class="abs btn-red" style="left:392px;top:464px">Learn More »</div>
    <div class="abs btn-red" style="left:609px;top:464px">Learn More »</div>
  </section>

  <section>
    <div class="abs band"></div>
    <div class="abs" style="left:561px;top:512px;width:1px;height:176px;background:#e4e1d8"></div>
    <p class="abs band-copy">Protecting and Defending Your Business Against Competitors, Rogue Employees, Cheating Business Partners, Devious Contracting Parties, and Overzealous Government Agencies.<br>Don't settle for lawyers who promise to work to solve your problems. I will work to prevent your problems in the first place. Learn more about litigation avoidance in my practice areas of law.</p>
    <p class="abs band-quote">A recent study shows that plaintiffs in most diversity cases never asked a judge to "certify a class" of those covered in the suit.</p>
  </section>

  <section>
    <div class="abs date" style="left:109px;top:722px"><small>18 JAN</small><span>2014</span></div>
    <div class="abs post-title" style="left:168px;top:723px">POST1</div>
    <p class="abs post-body" style="left:109px;top:774px">I give real, practical advice to keep you out of trouble, stay in business and make money. I won't bore you with legal theories, but will explain how the legal issues affect your business. I have a passion for helping businesses and other clients. If you are sued or have to sue another business, customer or ex-employee or business partner, I will develop the right, cost effective strategy with you.</p>
    <div class="abs post-rule" style="left:105px;top:840px;width:453px"></div>
    <div class="abs view-all" style="left:486px;top:836px">+View All</div>

    <div class="abs date" style="left:109px;top:857px"><small>18 JAN</small><span>2014</span></div>
    <div class="abs post-title" style="left:168px;top:856px">POST1</div>
    <p class="abs post-body" style="left:109px;top:912px">I give real, practical advice to keep you out of trouble, stay in business and make money. I won't bore you with legal theories, but will explain how the legal issues affect your business. I have a passion for helping businesses and other clients. If you are sued or have to sue another business, customer or ex-employee or business partner, I will develop the right, cost effective strategy with you.</p>
    <div class="abs post-rule" style="left:105px;top:979px;width:453px"></div>
    <div class="abs view-all" style="left:486px;top:975px">+View All</div>
  </section>

  <aside class="abs blog">
    <div class="abs blog-art" role="img" aria-label="Textured blog banner"></div>
    <div class="abs blog-name">RIVETSAND</div>
    <div class="abs blog-bar">Rivets and Sand: Notes for Owners</div>
    <div class="abs blog-inner"></div>
    <svg class="abs" style="left:6px;top:114px" width="22" height="18" viewBox="0 0 22 18" aria-hidden="true"><path d="M0 6 H12 V1 L22 9 L12 17 V12 H0 Z" fill="#222"/></svg>
    <div class="abs blog-head">You're Damned If You Don't Respond Appropriately to a Poor Rateline Review or Online Post.</div>
    <div class="abs blog-meta">Posted: January 18, 2014<br>in Lawsuits</div>
    <p class="abs blog-text">We live in crazy times for businesses. Any crackpot with a computer and internet connection can say anything that they want about your business in an online review, on social media, etc. That's the unfortunate reality for today's private businesses. The crackpots may even attack the business owner personally. Even worse, there is little you can do to stop it and, in many cases, you can't even get it removed (I won't bore you with a treatise on prior restraints of free speech)...</p>
    <div class="abs blog-foot"><span>Featured Resources</span><a href="#">+ View All</a></div>
  </aside>

  <footer>
    <div class="abs foot-nav">
      <span>Why Hire Me?</span><span>|</span><span>Success Stories</span><span>|</span><span>Practice Areas</span><span>|</span><span>Representative Clients</span><span>|</span><span>Services Provided</span><span>|</span><span>Contact Us</span><span>|</span><span>How To Find Us</span>
    </div>
    <div class="abs foot-contact">Questions? Call <b>617 555-0142</b> | <u>kbrandell@kbrandellegal.com</u></div>
    <div class="abs foot-brand">Karen J. Brandell<small>Law Office</small></div>
    <div class="abs legal">Copyright ©2014 Law Office of Karen J. Brandell - <u>All Rights Reserved</u> | <u>Terms of Use</u> | <u>Privacy Policy</u> | <u>Sitemap</u></div>
  </footer>

</div>
</body>
</html>
```